Fenwick Nutrition Therapy needs a business card design

I need a business card design for my private practice. Green is my favorite color. I would like the back of the card to include an area for future appointment dates and time. I provide nutrition therapy to individuals, groups and families. I work a lot with adolescents and women who have eating disorders, but also work with athletes.
Updates

Reason: I received several new designs and would like to take some time reviewing them.

Target Market(s)

I am working primarily with women, but also men (mostly athletes). I work with a lot of runners. I work with people who are 14-60's.

Industry/Entity Type

Nutrition

Font styles to use
Serif
Sans Serif

Colors
9bcb3c
acd037

Requirements
Nice to have
• I would love to have 'Fenwick' incorporated into the design since it is my last name. If possible, I'd love to have an actual moon if it looks professional.

A picture of food could also be on the card if it is simple, but not sure how it would look with Fenwick. I am open to ideas for both Fenwick and a picture of a food item.

Other font style are fine as long as they are easy to read.

```html
<!DOCTYPE html>
<html lang="en">
<head>
<meta charset="utf-8">
<title>Fenwick Nutrition Therapy – Business Card</title>
<link rel="stylesheet" href="https://fonts.googleapis.com/css2?family=Marcellus&family=Open+Sans:wght@400;600&display=swap">
<style>
  :root {
    --backdrop: #2b2b2b;
    --card-green: #acd037;
    --band-green: #8cbf2c;
    --ink: #111111;
    --ink-soft: #3a4a14;
    --moon: #f4f4f2;
  }
  * { box-sizing: border-box; margin: 0; padding: 0; }
  html, body { width: 1200px; height: 675px; overflow: hidden; }
  body {
    background: var(--backdrop);
    font-family: "Marcellus", serif;
    color: var(--ink);
    position: relative;
  }
  .card {
    position: absolute;
    top: 188px;
    width: 520px;
    height: 300px;
    background: var(--card-green);
    border-top: 9px solid var(--band-green);
    border-bottom: 14px solid var(--band-green);
  }
  .card--front { left: 60px; }
  .card--back { left: 620px; }

  /* Front */
  .front-moon {
    position: absolute;
    left: 50%;
    top: 42px;
    width: 84px;
    height: 84px;
    margin-left: -42px;
    border-radius: 50%;
    background: var(--moon);
  }
  .front-name {
    position: absolute;
    left: 0; right: 0;
    top: 150px;
    text-align: center;
    font-weight: 400;
  }
  .front-name span {
    display: inline-block;
    font-size: 25px;
    letter-spacing: 0.3px;
    padding: 0 6px 6px;
    border-bottom: 1.5px solid var(--ink);
  }

  /* Back */
  .back-brand {
    position: absolute;
    left: 40px;
    top: 18px;
  }
  .back-moon {
    width: 44px;
    height: 44px;
    margin-left: 50px;
    border-radius: 50%;
    background: var(--moon);
  }
  .back-name {
    display: inline-block;
    margin-top: 12px;
    font-size: 14.5px;
    padding: 0 2px 4px;
    border-bottom: 1px solid var(--ink);
  }
  .holder {
    position: absolute;
    left: 48px;
    top: 114px;
  }
  .holder-name { font-size: 16px; font-weight: 400; }
  .holder-role {
    font-family: "Open Sans", sans-serif;
    font-size: 10.5px;
    letter-spacing: 1.6px;
    color: var(--ink-soft);
    margin-top: 4px;
  }
  .contact {
    position: absolute;
    left: 40px;
    top: 170px;
    list-style: none;
    font-size: 12.5px;
  }
  .contact li { display: flex; align-items: center; height: 21px; }
  .contact .indent { padding-left: 40px; }
  .contact svg { width: 11px; height: 12px; margin-right: 10px; }
  .appointment {
    position: absolute;
    right: 42px;
    top: 176px;
    font-size: 11px;
  }
  .appointment div { display: flex; align-items: flex-end; height: 28px; }
  .appointment .line {
    display: inline-block;
    width: 104px;
    border-bottom: 1px solid var(--ink);
    margin-left: 5px;
  }
</style>
</head>
<body>
  <section class="card card--front" aria-label="Card front">
    <div class="front-moon"></div>
    <h1 class="front-name"><span>FENWICK NUTRITION THERAPY</span></h1>
  </section>

  <section class="card card--back" aria-label="Card back">
    <div class="back-brand">
      <div class="back-moon"></div>
      <div class="back-name">FENWICK NUTRITION THERAPY</div>
    </div>

    <div class="holder">
      <h2 class="holder-name">LOREM IPSUM DOLOR</h2>
      <p class="holder-role">Lorem ipsum dolor sit amet</p>
    </div>

    <ul class="contact">
      <li>ADDRESS:&nbsp;XXXXXXXXXXX</li>
      <li class="indent">
        <svg viewBox="0 0 11 14" aria-hidden="true"><rect x="1.5" y="0.5" width="8" height="13" rx="1.5" fill="none" stroke="#111"/><rect x="3" y="2.5" width="5" height="4" fill="#111"/><rect x="3" y="8.5" width="5" height="3" fill="#111"/></svg>XXXXXXXXXXX
      </li>
      <li class="indent">
        <svg viewBox="0 0 12 9" aria-hidden="true"><rect x="0.5" y="0.5" width="11" height="8" fill="none" stroke="#111"/><path d="M0.5 0.5 L6 5 L11.5 0.5" fill="none" stroke="#111"/></svg>XXXXXXXXXXX
      </li>
    </ul>

    <div class="appointment">
      <div>DATE:<span class="line"></span></div>
      <div>TIME:<span class="line"></span></div>
    </div>
  </section>
</body>
</html>
```